Olvar business stationery
Purified water company
Simple
Rodrigo Lemus
Gerente General
Calle 38 con Avenida Tzabalché
entre 164 y 166
Colonia Vista de Orquídeas
Mérida, Yucatán
rlem@purificadoraolvar-mx.com
www.purificadoraolvar-mx.com
- The logo font is Quadranta
- We would like all stationary, including letterhead, envelopes, business card, presentation folder, compliment card and fax cover
- Color gradient of blue
Light blue C=50 M=1 Y=0 K=0
Blue C=92 M=63 Y=1 K=0
Stroke light blue C=27 M=0 Y=1 K=0
siempre contigo...
- Name and image should be integrated in the design of the stationary
- Designers can split the name (quadranta font) and the waterfall image to use as they like during their designs

```html
<!DOCTYPE html>
<html lang="es">
<head>
<meta charset="utf-8">
<title>Olvar business stationery</title>
<link href="https://fonts.googleapis.com/css2?family=Comfortaa:wght@400;600;700&family=Quicksand:wght@400;500&display=swap" rel="stylesheet">
<style>
  :root {
    --page: #e9ecef;
    --blue-deep: #0c4f9e;
    --blue-mid: #1f6fc0;
    --blue-light: #4fb6ea;
    --stroke-light: #b8e3f7;
    --leaf-green: #9cbf2f;
    --white: #ffffff;
    --name-blue: #2a7bc9;
    --title-grey: #4a5563;
  }
  * { margin: 0; padding: 0; box-sizing: border-box; }
  html, body { width: 1200px; height: 901px; overflow: hidden; background: var(--page); }
  .canvas { position: relative; width: 1200px; height: 901px; }

  .card {
    position: absolute;
    width: 640px; height: 366px;
    border-radius: 18px;
    overflow: hidden;
    box-shadow: 0 6px 18px rgba(0,0,0,.18);
  }
  .card svg.art { position: absolute; inset: 0; width: 100%; height: 100%; }

  /* back of card */
  .card-back {
    left: 80px; top: 60px;
    background: linear-gradient(160deg, var(--blue-light) 0%, var(--blue-mid) 45%, var(--blue-deep) 100%);
  }
  .back-emblem {
    position: absolute; left: 245px; top: 55px;
    width: 150px; height: 150px; border-radius: 50%;
    background: radial-gradient(circle at 40% 35%, #e8f6fd 0%, #8fd0ef 55%, #4fa3d6 100%);
  }
  .tagline {
    position: absolute; left: 0; right: 0; top: 228px;
    text-align: center;
    font-family: "Comfortaa", sans-serif; font-size: 15px;
    color: var(--stroke-light); letter-spacing: .5px;
  }

  /* front of card */
  .card-front { left: 480px; top: 470px; background: var(--white); }
  .brand {
    position: absolute; left: 180px; top: 44px;
    display: flex; align-items: center; gap: 12px;
  }
  .brand-dot { width: 44px; height: 44px; border-radius: 50%; background: var(--blue-light); }
  .brand-name {
    font-family: "Comfortaa", sans-serif; font-weight: 700;
    font-size: 58px; color: var(--blue-light); letter-spacing: 1px;
  }
  .person { position: absolute; left: 150px; top: 128px; }
  .person-name {
    font-family: "Comfortaa", sans-serif; font-weight: 600;
    font-size: 25px; color: var(--name-blue);
  }
  .person-title {
    margin: 4px 0 0 92px;
    font-family: "Quicksand", sans-serif; font-size: 13px; color: var(--title-grey);
  }
  .contact {
    position: absolute; right: 52px; top: 200px;
    text-align: right; font-style: normal;
    font-family: "Quicksand", sans-serif; font-size: 12.5px; line-height: 16px;
    color: var(--white);
  }
  .contact .gap { height: 10px; }
  .icons {
    position: absolute; right: 16px; top: 276px;
    display: flex; flex-direction: column; gap: 4px;
  }
  .icons svg { width: 14px; height: 14px; display: block; }
</style>
</head>
<body>
<main class="canvas">

  <section class="card card-back" aria-label="Reverso de la tarjeta">
    <div class="back-emblem" role="img" aria-label="Ilustración de cascada con vegetación"></div>
    <p class="tagline">siempre contigo...</p>
  </section>

  <section class="card card-front" aria-label="Frente de la tarjeta">
    <svg class="art" viewBox="0 0 640 366" preserveAspectRatio="none" aria-hidden="true">
      <defs>
        <linearGradient id="band" x1="0" y1="0" x2="1" y2="1">
          <stop offset="0" stop-color="#2a86d2"/>
          <stop offset="1" stop-color="#0c4f9e"/>
        </linearGradient>
      </defs>
      <path d="M0 0 H300 C220 20 90 30 0 70 Z" fill="url(#band)"/>
      <path d="M0 82 C90 40 220 24 330 4" fill="none" stroke="#9cbf2f" stroke-width="3"/>
      <path d="M0 92 C100 48 240 30 360 6" fill="none" stroke="#b8e3f7" stroke-width="2"/>
      <path d="M0 290 C200 262 380 200 640 80 V366 H0 Z" fill="url(#band)"/>
      <path d="M0 278 C200 250 380 188 640 68" fill="none" stroke="#9cbf2f" stroke-width="3"/>
      <path d="M0 270 C200 240 380 178 640 58" fill="none" stroke="#b8e3f7" stroke-width="2"/>
    </svg>

    <div class="brand">
      <span class="brand-dot"></span>
      <span class="brand-name">Olvar</span>
    </div>

    <div class="person">
      <p class="person-name">Rodrigo Lemus</p>
      <p class="person-title">Gerente General</p>
    </div>

    <address class="contact">
      Calle 38 con Avenida Tzabalché<br>
      entre 164 y 166<br>
      Colonia Vista de Orquídeas<br>
      Mérida, Yucatán
      <div class="gap"></div>
      999-4172650<br>
      rlem@purificadoraolvar-mx.com<br>
      rlem58<br>
      www.purificadoraolvar-mx.com
    </address>

    <div class="icons" aria-hidden="true">
      <svg viewBox="0 0 14 14"><rect x="4" y="1" width="6" height="12" rx="1.5" fill="none" stroke="#fff" stroke-width="1.3"/><circle cx="7" cy="11" r=".8" fill="#fff"/></svg>
      <svg viewBox="0 0 14 14"><rect x="1" y="3" width="12" height="8" rx="1" fill="none" stroke="#fff" stroke-width="1.3"/><path d="M1 3.5 L7 8 L13 3.5" fill="none" stroke="#fff" stroke-width="1.2"/></svg>
      <svg viewBox="0 0 14 14"><circle cx="7" cy="7" r="5.5" fill="none" stroke="#fff" stroke-width="1.3"/><circle cx="7" cy="7" r="2" fill="#fff"/></svg>
      <svg viewBox="0 0 14 14"><circle cx="7" cy="7" r="5.5" fill="none" stroke="#fff" stroke-width="1.3"/><path d="M1.5 7 H12.5 M7 1.5 C4 4 4 10 7 12.5 M7 1.5 C10 4 10 10 7 12.5" fill="none" stroke="#fff" stroke-width="1"/></svg>
    </div>
  </section>

</main>
</body>
</html>
```